The Verdant Ledger App - Modernization & Graphics User Interface Friendliness Updates

We are Verdant Ledger, and we want to bring a new branding look and graphical user interface to the Verdant Ledger App. The app is a quick reference encyclopedia for all things produce. Boasting articles on over 2,000 produce items, with information ranging from taste and application to geographical and cultural significance. Included in its features are over 10 thousand recipes, and the Verdant Ledger App Harvest Circle – a global initiative to connect farmer, customer, and chef in one sustainable and easy to use application. The design needs to bring a greater sense of social connection – encouraging the user to participate in the 'Harvest Circled' experience voluntarily. The design should reflect a sense of authority reflecting the authenticity and reliability of the provided information, it's writing, and its sources. Download the App here: vledgr.example/install

Target Market(s)

Women and Men between ages 21-55.

Industry/Entity Type

Education

Font styles to use
Serif
Sans Serif

Colors

Designer to choose colors to be used in the design.

Requirements
Must have
• An updated user interface, the intuitive usability of the app is currently non-existent. We are looking to reflect as the authority on produce. The app design must reflect a professional, user-friendly, up-to-date, and trustworthy feel.
Nice to have
• To incorporate the social draw of the Harvest Circle we would like to include on the home page "Social Bubbles" (think Pictoloop stories) which updates with shared photos of produce and their location.
Should not have
• An overly complicated theme, distracting or unprofessional colors, and images.

```html
<!DOCTYPE html>
<html lang="en">
<head>
<meta charset="utf-8">
<title>Verdant Ledger App – Interface Screens</title>
<link href="https://fonts.googleapis.com/css2?family=Poppins:wght@400;500;600;700&display=swap" rel="stylesheet">
<style>
:root{
  --bg-top:#a9d7ab;
  --bg-mid:#5fb468;
  --bg-bottom:#2f8f3d;
  --mint:#8fd3a0;
  --mint-soft:#cbe9d2;
  --mint-screen:#c6e6cd;
  --green-text:#6cc283;
  --ink:#1f2421;
  --grey:#9a9f9b;
  --grey-light:#e6e9e6;
  --panel:#f3f5f3;
  --red:#e53935;
  --white:#ffffff;
  --key-bg:#5d6c5c;
  --key:#7d8b7c;
}
*{box-sizing:border-box;margin:0;padding:0}
html,body{width:711px;height:1200px;overflow:hidden}
body{
  font-family:"Poppins",Arial,sans-serif;
  color:var(--ink);
  background:linear-gradient(180deg,var(--bg-top) 0%,var(--bg-mid) 40%,var(--bg-bottom) 100%);
  position:relative;
}
.brand{position:absolute;top:120px;left:0;width:100%;text-align:center}
.brand-name{display:inline-flex;align-items:center;gap:10px;font-weight:600;font-size:34px;color:var(--ink);letter-spacing:.5px}
.brand-dot{width:16px;height:16px;border-radius:50%;background:var(--ink)}
.brand-url{font-size:11px;color:var(--ink);margin-top:4px;letter-spacing:2px}

.row{position:absolute;left:0;width:100%;display:flex;justify-content:center;gap:14px}
.row-top{top:250px}
.row-bottom{top:660px}
.screen{position:relative;width:160px;height:360px;background:var(--white);border-radius:14px;overflow:hidden;box-shadow:0 6px 18px rgba(0,0,0,.18)}
.abs{position:absolute}
.icon{width:10px;height:10px;stroke:currentColor;fill:none;stroke-width:1.6;stroke-linecap:round;stroke-linejoin:round;display:block}
.back,.hamburger,.close{width:10px;height:10px;top:41px}
.back{left:12px;color:var(--green-text)}
.bell{right:12px;top:40px;width:11px;height:11px;color:var(--ink)}
.bell .icon{width:11px;height:11px}
.badge{position:absolute;right:-3px;top:-3px;width:6px;height:6px;border-radius:50%;background:var(--red)}
.title{left:0;width:100%;top:41px;text-align:center;font-size:7px;line-height:10px;font-weight:600;letter-spacing:.3px}
.title.green{color:var(--green-text);font-weight:500}

.label{left:14px;font-size:4.5px;color:#c3c7c4;letter-spacing:.3px}
.field{left:12px;width:136px;height:18px;border-radius:3px;box-shadow:0 1px 4px rgba(0,0,0,.08);font-size:8px;padding:4px 4px;color:var(--ink);white-space:nowrap;overflow:hidden}
.forgot{right:14px;font-size:5.5px;color:var(--green-text)}
.account{left:14px;font-size:5px;font-weight:600}
.register{left:14px;font-size:9px;color:var(--green-text);line-height:1}
.login{right:14px;width:42px;height:16px;border-radius:9px;background:var(--mint);color:var(--white);font-size:5.5px;font-weight:600;display:flex;align-items:center;justify-content:center;gap:4px;box-shadow:0 2px 5px rgba(80,170,110,.35)}
.login .icon{width:9px;height:7px;stroke:var(--white)}
.skip{left:0;width:100%;text-align:center;font-size:7px;color:var(--green-text)}

.keyboard{left:6px;right:6px;top:222px;height:80px;background:var(--key-bg);padding:3px 3px;display:flex;flex-direction:column;gap:3px}
.krow{display:flex;gap:2px;justify-content:center}
.key{flex:0 0 11px;height:15px;background:var(--key);border-radius:2px;color:#e8ece8;font-size:6.5px;display:flex;align-items:center;justify-content:center}
.key.wide{flex:0 0 17px;font-size:4.5px}
.key.space{flex:1 1 auto;font-size:5px}
.key.ret{flex:0 0 30px;font-size:5px}

.photo{border-radius:4px}
.ph-orange{background:linear-gradient(135deg,#ffd6a0,#f8b25a)}
.ph-plant{background:linear-gradient(135deg,#cfe2c0,#6f9b55 60%,#c94a3a)}
.ph-fruit{background:linear-gradient(135deg,#f4c04a,#c8372a 55%,#5c8f3a)}
.ph-veg{background:linear-gradient(135deg,#f39a2a,#b8232a 55%,#3f7d32)}
.ph-berry{background:linear-gradient(135deg,#7ea34c,#2a2a3a 60%,#3a3348)}
.ph-dish{background:linear-gradient(135deg,#d95a3a,#efc08a 60%,#7aa24b)}
.ph-greens{background:radial-gradient(ellipse at center,#3f7c2e 0%,#6fa34c 45%,rgba(255,255,255,0) 72%)}
.ph-map{background:linear-gradient(180deg,rgba(255,255,255,1) 0%,#dfe6e0 35%,#cfd8d1 100%)}
.ph-pepper{background:linear-gradient(135deg,#f7c9cd,#e8383a)}

.hamburger{left:12px;color:var(--green-text)}
.h-section{left:12px;font-size:9.5px;font-weight:600}
.grid-ic{right:12px;width:10px;height:10px;color:var(--green-text)}
.cat{width:42px;text-align:center;font-size:4.5px}
.cat .photo{height:52px;margin-bottom:4px;box-shadow:0 2px 5px rgba(0,0,0,.12)}
.stars{color:var(--green-text);font-size:4.5px;letter-spacing:.5px}

.fab{right:12px;width:20px;height:20px;border-radius:50%;background:var(--red);color:var(--white);display:flex;align-items:center;justify-content:center;box-shadow:0 2px 6px rgba(229,57,53,.4)}
.fab .icon{width:9px;height:9px;stroke:var(--white)}
.nav{left:0;right:0;bottom:0;height:34px;background:var(--white);border-top:1px solid var(--grey-light);display:flex;justify-content:space-around;align-items:center;padding:0 6px}
.nav-item{display:flex;flex-direction:column;align-items:center;gap:2px;font-size:4.6px;color:var(--ink)}
.nav-item .icon{width:8px;height:8px}
.nav-item.active{color:var(--green-text)}

.stats{left:0;width:100%;display:flex;justify-content:center;gap:22px;font-size:4.8px;text-align:center}
.stats .icon{width:9px;height:9px;color:var(--green-text);margin:0 auto 2px}
.tabs{left:12px;right:12px;display:flex;justify-content:space-between;font-size:4.8px;font-weight:600}
.tabs .on{border-bottom:1.5px solid var(--ink);padding-bottom:2px}
.desc{left:12px;right:12px;font-size:4.3px;line-height:1.65;color:#555}
.desc .more{color:var(--green-text)}

.close{left:14px;color:var(--green-text)}
.menu{left:18px;top:76px;border-left:1.5px solid var(--ink)}
.menu li{list-style:none;font-size:5.8px;font-weight:500;padding:0 0 0 10px;height:20px;white-space:nowrap}
.menu li:first-child{font-weight:600}
.preview{left:96px;top:76px;width:80px;height:200px;background:var(--white);box-shadow:-3px 4px 10px rgba(0,0,0,.14);transform:rotate(-6deg);border-radius:4px;padding:8px 6px}
.preview .cap{font-size:5px;font-weight:600;margin-bottom:4px}

.panel{left:0;right:0;top:0;bottom:34px;background:var(--panel)}
.note{left:14px;right:12px;display:flex;gap:8px;align-items:flex-start}
.avatar{flex:0 0 18px;height:18px;border-radius:50%;background:linear-gradient(135deg,#e8b79a,#9c6a52)}
.avatar.blank{background:var(--white);border:1px solid var(--grey-light);display:flex;align-items:center;justify-content:center;color:var(--ink)}
.avatar.blank .icon{width:8px;height:8px}
.note-text{font-size:4.8px;line-height:1.4;color:#555;padding-top:2px}
.note-text b{color:var(--ink);font-weight:600}
.note-time{display:block;font-size:3.8px;color:#b4b8b5;margin-top:1px}

.mint-panel{left:0;right:0;top:0;bottom:34px;background:var(--mint-screen)}
.search-field{left:12px;right:12px;top:72px;height:20px;border-radius:11px;border:1px solid #e4f3e7;font-size:7px;font-weight:500;padding:5px 10px}
.s-label{left:14px;font-size:4.8px;font-weight:600}
.chips{left:12px;display:flex;gap:4px;white-space:nowrap}
.chip{height:10px;padding:0 8px;border-radius:6px;font-size:4.2px;display:flex;align-items:center;border:1px solid #e4f3e7;color:var(--ink)}
.chip.fill{background:var(--mint);border-color:var(--mint);color:var(--white);font-weight:600}
</style>
</head>
<body>

<svg width="0" height="0" style="position:absolute" aria-hidden="true">
  <defs>
    <symbol id="i-back" viewBox="0 0 12 12"><path d="M11 6H1M5 2L1 6l4 4"/></symbol>
    <symbol id="i-arrow" viewBox="0 0 14 10"><path d="M1 5h12M9 1l4 4-4 4"/></symbol>
    <symbol id="i-bell" viewBox="0 0 12 12"><path d="M3 8V5.5a3 3 0 016 0V8l1 1.2H2zM5 10.5a1 1 0 002 0"/></symbol>
    <symbol id="i-menu" viewBox="0 0 12 12"><path d="M1 3h10M1 6h10M1 9h10"/></symbol>
    <symbol id="i-grid" viewBox="0 0 12 12"><path d="M1 3h4M7 3h4M1 6h4M7 6h4M1 9h4M7 9h4"/></symbol>
    <symbol id="i-search" viewBox="0 0 12 12"><circle cx="5" cy="5" r="3.5"/><path d="M8 8l3 3"/></symbol>
    <symbol id="i-fruit" viewBox="0 0 12 12"><circle cx="6" cy="7" r="4"/><path d="M6 3c0-1 .6-2 2-2"/></symbol>
    <symbol id="i-chat" viewBox="0 0 12 12"><path d="M1.5 2h9v6h-5l-3 2.5V8h-1z"/></symbol>
    <symbol id="i-eye" viewBox="0 0 12 12"><path d="M1 6s2-3.5 5-3.5S11 6 11 6s-2 3.5-5 3.5S1 6 1 6z"/><circle cx="6" cy="6" r="1.5"/></symbol>
    <symbol id="i-bowl" viewBox="0 0 12 12"><path d="M1 6h10a5 4 0 01-10 0zM7 5l3-3"/></symbol>
    <symbol id="i-dots" viewBox="0 0 12 12"><path d="M2 6h.1M6 6h.1M10 6h.1"/></symbol>
    <symbol id="i-heart" viewBox="0 0 12 12"><path d="M6 10S1 7 1 4a2.5 2.5 0 015-1 2.5 2.5 0 015 1c0 3-5 6-5 6z"/></symbol>
    <symbol id="i-share" viewBox="0 0 12 12"><circle cx="9" cy="2.5" r="1.3"/><circle cx="3" cy="6" r="1.3"/><circle cx="9" cy="9.5" r="1.3"/><path d="M4.2 5.3l3.6-2M4.2 6.7l3.6 2"/></symbol>
    <symbol id="i-close" viewBox="0 0 12 12"><path d="M2 2l8 8M10 2l-8 8"/></symbol>
    <symbol id="i-user" viewBox="0 0 12 12"><circle cx="6" cy="4" r="2.2"/><path d="M2 11c0-2.5 1.8-4 4-4s4 1.5 4 4"/></symbol>
  </defs>
</svg>

<header class="brand">
  <div class="brand-name"><span class="brand-dot"></span>Verdant Ledger</div>
  <div class="brand-url">vledgr.example/install</div>
</header>

<section class="row row-top">

  <article class="screen">
    <span class="abs back"><svg class="icon"><use href="#i-back"/></svg></span>
    <div class="abs title">SIGN IN</div>
    <div class="abs label" style="top:84px">EMAIL ADDRESS</div>
    <div class="abs field" style="top:94px">elin.moss@mailbox.example</div>
    <div class="abs label" style="top:134px">PASSWORD</div>
    <div class="abs field" style="top:144px"></div>
    <div class="abs forgot" style="top:156px">Forgot?</div>
    <div class="abs account" style="top:196px">Don't have an account</div>
    <div class="abs register" style="top:203px">Register</div>
    <div class="abs login" style="top:196px">LOGIN <svg class="icon"><use href="#i-arrow"/></svg></div>
    <div class="abs skip" style="top:270px">Skip</div>
  </article>

  <article class="screen">
    <span class="abs back"><svg class="icon"><use href="#i-back"/></svg></span>
    <div class="abs title">SIGN IN</div>
    <div class="abs label" style="top:84px">EMAIL ADDRESS</div>
    <div class="abs field" style="top:94px">elin.moss@mailbox.example</div>
    <div class="abs label" style="top:134px">PASSWORD</div>
    <div class="abs field" style="top:144px"></div>
    <div class="abs forgot" style="top:156px">Forgot?</div>
    <div class="abs account" style="top:192px">Don't have an account</div>
    <div class="abs register" style="top:199px">Register</div>
    <div class="abs login" style="top:192px">LOGIN <svg class="icon"><use href="#i-arrow"/></svg></div>
    <div class="abs keyboard">
      <div class="krow"><span class="key">q</span><span class="key">w</span><span class="key">e</span><span class="key">r</span><span class="key">t</span><span class="key">y</span><span class="key">u</span><span class="key">i</span><span class="key">o</span><span class="key">p</span></div>
      <div class="krow"><span class="key">a</span><span class="key">s</span><span class="key">d</span><span class="key">f</span><span class="key">g</span><span class="key">h</span><span class="key">j</span><span class="key">k</span><span class="key">l</span></div>
      <div class="krow"><span class="key wide">⇧</span><span class="key">z</span><span class="key">x</span><span class="key">c</span><span class="key">v</span><span class="key">b</span><span class="key">n</span><span class="key">m</span><span class="key wide">⌫</span></div>
      <div class="krow"><span class="key wide">123</span><span class="key">☺</span><span class="key">•</span><span class="key space">space</span><span class="key ret">return</span></div>
    </div>
  </article>

  <article class="screen">
    <span class="abs hamburger"><svg class="icon"><use href="#i-menu"/></svg></span>
    <span class="abs bell"><svg class="icon"><use href="#i-bell"/></svg><span class="badge"></span></span>
    <div class="abs h-section" style="top:58px">Recently spotted</div>
    <div class="abs photo ph-orange" style="left:12px;top:78px;width:66px;height:60px" role="img" aria-label="Orange slices beside a kitchen quote card"></div>
    <div class="abs photo ph-plant" style="left:82px;top:78px;width:66px;height:60px" role="img" aria-label="Fresh produce spotted growing on the plant"></div>
    <div class="abs h-section" style="top:150px">Categories</div>
    <span class="abs grid-ic" style="top:153px"><svg class="icon"><use href="#i-grid"/></svg></span>
    <div class="abs cat" style="left:12px;top:168px"><div class="photo ph-fruit" role="img" aria-label="Assorted fruit"></div>All Fruit<div class="stars">★★★★★</div></div>
    <div class="abs cat" style="left:59px;top:168px"><div class="photo ph-veg" role="img" aria-label="Assorted vegetables"></div>All Vegetable<div class="stars">★★★☆☆</div></div>
    <div class="abs cat" style="left:106px;top:168px"><div class="photo ph-berry" role="img" aria-label="Foraged blackberries and leaves"></div>Foraged<div class="stars">★★★★☆</div></div>
    <div class="abs photo ph-dish" style="left:12px;top:248px;width:42px;height:30px" role="img" aria-label="Recipe dish"></div>
    <div class="abs photo ph-veg" style="left:59px;top:248px;width:42px;height:30px" role="img" aria-label="Salad dish"></div>
    <div class="abs photo ph-dish" style="left:106px;top:248px;width:42px;height:30px" role="img" aria-label="Vegetable dish"></div>
    <div class="abs fab" style="top:252px"><svg class="icon"><use href="#i-search"/></svg></div>
    <nav class="abs nav">
      <span class="nav-item active"><svg class="icon"><use href="#i-fruit"/></svg>Produce</span>
      <span class="nav-item"><svg class="icon"><use href="#i-chat"/></svg>Chirper</span>
      <span class="nav-item"><svg class="icon"><use href="#i-eye"/></svg>Spotted</span>
      <span class="nav-item"><svg class="icon"><use href="#i-bowl"/></svg>Recipes</span>
      <span class="nav-item"><svg class="icon"><use href="#i-dots"/></svg>More</span>
    </nav>
  </article>

  <article class="screen">
    <span class="abs back"><svg class="icon"><use href="#i-back"/></svg></span>
    <div class="abs title green">GAI LAN</div>
    <span class="abs bell"><svg class="icon"><use href="#i-bell"/></svg></span>
    <div class="abs ph-greens" style="left:30px;top:56px;width:100px;height:62px" role="img" aria-label="Bunch of gai lan greens"></div>
    <div class="abs stats" style="top:128px">
      <span><svg class="icon"><use href="#i-heart"/></svg>125</span>
      <span><svg class="icon"><use href="#i-chat"/></svg>95</span>
      <span><svg class="icon"><use href="#i-share"/></svg>Share</span>
    </div>
    <div class="abs tabs" style="top:160px"><span class="on">DESCRIPTION</span><span>INGREDIENTS</span><span>NUTRITIONS</span></div>
    <div class="abs ph-map" style="left:0;right:0;top:190px;height:136px" role="img" aria-label="Faint world map showing growing regions"></div>
    <p class="abs desc" style="top:176px">Gai lan, also called Chinese broccoli, grows thick glossy leaves and tender stalks that stay crisp when lightly steamed or stir fried. <span class="more">more</span></p>
    <div class="abs fab" style="top:256px"><svg class="icon"><use href="#i-search"/></svg></div>
    <nav class="abs nav">
      <span class="nav-item active"><svg class="icon"><use href="#i-fruit"/></svg>Produce</span>
      <span class="nav-item"><svg class="icon"><use href="#i-chat"/></svg>Chirper</span>
      <span class="nav-item"><svg class="icon"><use href="#i-eye"/></svg>Spotted</span>
      <span class="nav-item"><svg class="icon"><use href="#i-bowl"/></svg>Recipes</span>
      <span class="nav-item"><svg class="icon"><use href="#i-dots"/></svg>More</span>
    </nav>
  </article>
</section>

<section class="row row-bottom">

  <article class="screen">
    <span class="abs close"><svg class="icon"><use href="#i-close"/></svg></span>
    <span class="abs bell"><svg class="icon"><use href="#i-bell"/></svg><span class="badge"></span></span>
    <div class="abs preview">
      <div class="cap">Hot Recipes</div>
      <div style="display:flex;gap:3px;margin-bottom:10px">
        <div class="photo ph-orange" style="width:32px;height:46px" role="img" aria-label="Orange recipe card"></div>
        <div class="photo ph-pepper" style="width:32px;height:46px" role="img" aria-label="Red bell pepper"></div>
      </div>
      <div class="cap">Categories</div>
      <div style="display:flex;gap:3px;margin-bottom:6px">
        <div class="photo ph-dish" style="width:21px;height:34px" role="img" aria-label="Dish"></div>
        <div class="photo ph-veg" style="width:21px;height:34px" role="img" aria-label="Salad"></div>
        <div class="photo ph-dish" style="width:21px;height:34px" role="img" aria-label="Vegetables"></div>
      </div>
      <div style="display:flex;gap:3px">
        <div class="photo ph-dish" style="width:21px;height:34px" role="img" aria-label="Dish"></div>
        <div class="photo ph-veg" style="width:21px;height:34px" role="img" aria-label="Salad"></div>
        <div class="photo ph-plant" style="width:21px;height:34px" role="img" aria-label="Greens"></div>
      </div>
    </div>
    <ul class="abs menu">
      <li>About Us</li><li>Contact Us</li><li>Multimedia</li><li>Press Info</li>
      <li>WasteLessVL</li><li>Take a Virtual Tour</li><li>New Customer</li><li>Application</li>
    </ul>
    <nav class="abs nav">
      <span class="nav-item active"><svg class="icon"><use href="#i-fruit"/></svg>Produce</span>
      <span class="nav-item"><svg class="icon"><use href="#i-chat"/></svg>Chirper</span>
      <span class="nav-item"><svg class="icon"><use href="#i-eye"/></svg>Spotted</span>
      <span class="nav-item"><svg class="icon"><use href="#i-bowl"/></svg>Recipes</span>
      <span class="nav-item"><svg class="icon"><use href="#i-dots"/></svg>More</span>
    </nav>
  </article>

  <article class="screen">
    <div class="abs panel"></div>
    <span class="abs back"><svg class="icon"><use href="#i-back"/></svg></span>
    <div class="abs title green">NOTIFICATIONS</div>
    <span class="abs bell"><svg class="icon"><use href="#i-bell"/></svg><span class="badge"></span></span>
    <div class="abs note" style="top:74px"><span class="avatar" role="img" aria-label="Profile photo"></span><p class="note-text"><b>Nora Lindqvist</b> like your post<span class="note-time">1 hour ago</span></p></div>
    <div class="abs note" style="top:114px"><span class="avatar" role="img" aria-label="Profile photo"></span><p class="note-text"><b>Pavel Storm</b> comment on your curry pudding post and follow you.<span class="note-time">1 hour ago</span></p></div>
    <div class="abs note" style="top:160px"><span class="avatar" role="img" aria-label="Profile photo"></span><p class="note-text"><b>Milo Arden</b> like your post<span class="note-time">1 hour ago</span></p></div>
    <div class="abs note" style="top:200px"><span class="avatar" role="img" aria-label="Profile photo"></span><p class="note-text"><b>Pavel Storm</b> comment on your post and follow you.<span class="note-time">1 hour ago</span></p></div>
    <div class="abs note" style="top:244px"><span class="avatar blank"><svg class="icon"><use href="#i-user"/></svg></span><p class="note-text"><b>Pavel Storm</b> follow you.<span class="note-time">2 days ago</span></p></div>
    <div class="abs fab" style="top:264px"><svg class="icon"><use href="#i-search"/></svg></div>
    <nav class="abs nav">
      <span class="nav-item active"><svg class="icon"><use href="#i-fruit"/></svg>Produce</span>
      <span class="nav-item"><svg class="icon"><use href="#i-chat"/></svg>Chirper</span>
      <span class="nav-item"><svg class="icon"><use href="#i-eye"/></svg>Spotted</span>
      <span class="nav-item"><svg class="icon"><use href="#i-bowl"/></svg>Recipes</span>
      <span class="nav-item"><svg class="icon"><use href="#i-dots"/></svg>More</span>
    </nav>
  </article>

  <article class="screen">
    <div class="abs mint-panel"></div>
    <span class="abs back" style="color:var(--ink)"><svg class="icon"><use href="#i-back"/></svg></span>
    <div class="abs title">SEARCH</div>
    <span class="abs bell"><svg class="icon"><use href="#i-bell"/></svg></span>
    <div class="abs search-field">PASTA</div>
    <div class="abs s-label" style="top:110px">NUTRITIONS</div>
    <div class="abs chips" style="top:122px"><span class="chip fill">PROTEIN</span><span class="chip fill">CARBOHYDRATES</span><span class="chip fill">FIBER</span><span class="chip">GL</span></div>
    <div class="abs s-label" style="top:152px">DURATIONS</div>
    <div class="abs chips" style="top:164px"><span class="chip">10 min</span><span class="chip fill">15 min</span><span class="chip">20 min</span><span class="chip">30 min</span></div>
    <div class="abs fab" style="top:264px"><svg class="icon"><use href="#i-search"/></svg></div>
    <nav class="abs nav">
      <span class="nav-item active"><svg class="icon"><use href="#i-fruit"/></svg>Produce</span>
      <span class="nav-item"><svg class="icon"><use href="#i-chat"/></svg>Chirper</span>
      <span class="nav-item"><svg class="icon"><use href="#i-eye"/></svg>Spotted</span>
      <span class="nav-item"><svg class="icon"><use href="#i-bowl"/></svg>Recipes</span>
      <span class="nav-item"><svg class="icon"><use href="#i-dots"/></svg>More</span>
    </nav>
  </article>
</section>

</body>
</html>
```